Veltrana Trade Show Banner 5ft wide by 8ft tall (additional brochure design available to winner)

Design and layout of 5ft wide x 8ft high (wxh) flat vinyl banner for Integrative medicine conference geared towards compounding pharmacists looking to expand their patient consultation practices. Our primary product is a patient care platform (software) that collects, creates, tracks, manages and analyzes patient health related information. Our platform allows providers to treat more efficiently and increase revenues through patient consultation, compounded prescriptions, and lab testing. We also offer a professional supplement line in which recommendations are made by our platform. Veltrana also offers provider training and practice setup in BHRT/Thyroid/Integrative Medicine.

I have attached our logo (Veltrana Crest) and a copy of two our supplement labels so you can see the different color schemes (we want to focus on royal blue and silver)

The final design should convey quality patient care, medical professionalism, and increased/additional revenues

Target Market(s)

Compounding and Consulting Pharmacists that want to expand or start their own patient consulting practices

Industry/Entity Type

Healthcare

Colors
0355a3
dbdbdb

Requirements
Must have
• Logo, Color Scheme, Compelling image, Patient Care Platform
Nice to have
• inclusion of Supplement line (veltrana wellness formulas), revenue streams (icons, images, maybe header)

```html
<!DOCTYPE html>
<html lang="en">
<head>
<meta charset="utf-8">
<title>Veltrana Trade Show Banner</title>
<link href="https://fonts.googleapis.com/css2?family=Jost:wght@400;500;700&display=swap" rel="stylesheet">
<style>
  :root {
    --royal: #0355a3;
    --royal-deep: #1a2a86;
    --royal-mid: #2740b0;
    --silver: #dbdbdb;
    --navy-text: #1b2466;
    --body-text: #1c1c24;
    --white: #ffffff;
    --stage: #2a2a2c;
  }
  * { margin: 0; padding: 0; box-sizing: border-box; }
  html, body { width: 800px; height: 1200px; overflow: hidden; }
  body { background: var(--stage); font-family: "Jost", sans-serif; position: relative; }

  .banner {
    position: absolute; left: 65px; top: 62px; width: 673px; height: 1078px;
    background: radial-gradient(ellipse at 50% 40%, var(--royal-mid) 0%, var(--royal-deep) 75%);
    overflow: hidden; color: var(--white);
  }
  .banner-shapes { position: absolute; inset: 0; }

  .brand-name {
    position: absolute; top: 86px; left: 0; width: 100%;
    text-align: center; font-weight: 700; font-size: 52px; line-height: 64px;
    letter-spacing: 2px; color: var(--white);
  }

  .headline {
    position: absolute; top: 218px; left: 0; width: 100%;
    text-align: center; font-weight: 700; font-size: 43px; line-height: 52px; letter-spacing: 0.5px;
  }
  .subhead {
    position: absolute; top: 280px; left: 59px; width: 570px;
    font-size: 20px; line-height: 26px; font-weight: 400; letter-spacing: 0.3px;
  }
  .services {
    position: absolute; top: 355px; left: 59px; width: 300px;
    font-size: 22.5px; line-height: 31px; font-weight: 400;
  }

  .photo-backdrop {
    position: absolute; left: 0; top: 470px; width: 673px; height: 480px;
    background: linear-gradient(90deg, #f4f6f8 0%, #e8eef0 45%, #dfe7e6 70%, #e9ecef 100%);
    clip-path: path("M0,35 Q336,-5 673,35 L673,420 Q336,490 0,420 Z");
  }
  .photo-person {
    position: absolute; left: 318px; top: 360px; width: 330px; height: 575px;
    border-radius: 140px 140px 0 0;
    background: linear-gradient(180deg, #d9c2b4 0%, #eef0f2 30%, #f6f6f7 60%, #e8dbe6 100%);
  }

  .offer-title {
    position: absolute; top: 574px; left: 59px;
    font-weight: 700; font-size: 29px; line-height: 36px; color: var(--navy-text); letter-spacing: 0.5px;
  }
  .offer-text {
    position: absolute; top: 611px; left: 59px; width: 320px;
    font-size: 23px; line-height: 30px; color: var(--body-text); font-weight: 500;
  }
  .offer-text strong { color: var(--navy-text); font-weight: 700; }

  .web-address {
    position: absolute; top: 1003px; left: 0; width: 100%;
    text-align: center; font-size: 29px; line-height: 36px; font-weight: 500; letter-spacing: 0.3px;
  }
  .web-address b { font-weight: 700; }
</style>
</head>
<body>
  <main class="banner">
    <svg class="banner-shapes" width="673" height="1078" viewBox="0 0 673 1078" aria-hidden="true">
      <defs>
        <linearGradient id="silverSweep" x1="0" y1="0" x2="1" y2="0">
          <stop offset="0" stop-color="#c9cbd0"/>
          <stop offset="0.5" stop-color="#ffffff"/>
          <stop offset="1" stop-color="#c9cbd0"/>
        </linearGradient>
        <linearGradient id="silverLeft" x1="0" y1="0" x2="1" y2="0">
          <stop offset="0" stop-color="#c9cbd0"/>
          <stop offset="1" stop-color="#ffffff"/>
        </linearGradient>
        <linearGradient id="silverRight" x1="0" y1="0" x2="1" y2="0">
          <stop offset="0" stop-color="#ffffff"/>
          <stop offset="1" stop-color="#c9cbd0"/>
        </linearGradient>
      </defs>
      <!-- top swooshes, stopping short of the wordmark -->
      <path d="M0,68 Q90,96 180,106 Q90,108 0,100 Z" fill="url(#silverLeft)"/>
      <path d="M673,52 Q583,90 493,106 Q583,104 673,88 Z" fill="url(#silverRight)"/>
      <!-- band frame -->
      <path d="M0,495 Q336,450 673,495 L673,512 Q336,466 0,512 Z" fill="url(#silverSweep)"/>
      <path d="M0,884 Q336,960 673,884 L673,905 Q336,982 0,905 Z" fill="url(#silverSweep)"/>
    </svg>

    <div class="brand-name">VELTRANA</div>

    <h1 class="headline">PATIENT CARE PLATFORM</h1>
    <p class="subhead">That Collects, Creates, Tracks, Manages and Analyzes<br>Patient Health Related Information.</p>
    <p class="services">Patient consultation,<br>compounded prescriptions,<br>and lab testing.</p>

    <div class="photo-backdrop" role="img" aria-label="Softly blurred pharmacy shelves in the background"></div>
    <div class="photo-person" role="img" aria-label="Smiling pharmacist in a white coat and pink shirt with arms crossed"></div>

    <h2 class="offer-title">WE ALSO OFFER A</h2>
    <p class="offer-text">professional<br>supplement line in which<br>recommendations are<br>made by our platform.<br>Veltrana also offers<br>provider training and<br>practice setup in<br><strong>BHRT/Thyroid/<br>Integrative Medicine.</strong></p>

    <p class="web-address">www.<b>VeltranaWellnessFormulas</b>.com</p>
  </main>
</body>
</html>
```